Nanna Keyplate, An IT Company Has New Logo, Need Fresh Business Cards

IT company is called Nanna Keyplate and is displayed nicely with the new logo from here on artflock. Would like a fresh business card look that encompasses the idea that we want clients to Cherish Every Gadget. I love the use of circuitry with hearts as endpoints and x's and o's. It needs to have room for my certification logos of which there are 4 and a KMB Alumni log. I am attaching my current card to illustrate how it has always captured attention, but that was in the early stages of business when I was doing more residential work. I am focused on businesses now, so a level of professionalism is necessary. I would also like the card to lend itself well to additional stationary, email signature, ticketing template for my workboard, etc. For the time being, I need the card for an upcoming conference so that work will come later. Color scheme should be that of the new logo. Thank you and I look forward to the designs.

Target Market(s)

Businesses looking for IT services.

Industry/Entity Type

Information Technology

Contact Information for Business Card

Requirements
Must have
• New logo colors and a warm feel. Possibly a tad feminine as I am female, but appealing to males.
Nice to have
• I would like techy, but no too much so. I like friendly and connecting feels. People LOVED my old card and called me because it gave them a warm feeling.

```html
<!DOCTYPE html>
<html lang="en">
<head>
<meta charset="utf-8">
<title>Nanna Keyplate — Business Cards</title>
<link href="https://fonts.googleapis.com/css2?family=Open+Sans:wght@400;600&display=swap" rel="stylesheet">
<style>
  :root {
    --canvas: #e4e4e4;
    --card-white: #fbfbfb;
    --sky: #84c9ea;
    --sky-deep: #5fb6e0;
    --ink: #2e2e2e;
    --ink-soft: #6b6b6b;
    --badge-gold: #b89a62;
    --badge-grey: #cfd3d6;
    --white: #ffffff;
  }
  * { box-sizing: border-box; margin: 0; padding: 0; }
  html, body { width: 1200px; height: 900px; overflow: hidden; }
  body {
    background: var(--canvas);
    font-family: "Open Sans", Arial, sans-serif;
    position: relative;
  }
  .card {
    position: absolute;
    width: 520px;
    height: 298px;
    border-radius: 4px;
    box-shadow: 0 10px 30px rgba(0,0,0,0.12);
  }

  /* ---------- Front (contact side) ---------- */
  .card-front {
    left: 50px;
    top: 300px;
    background: var(--card-white);
  }
  .holder-name {
    position: absolute; left: 30px; top: 26px;
    font-size: 17px; font-weight: 600; color: var(--sky-deep); letter-spacing: 1px;
  }
  .holder-role {
    position: absolute; left: 30px; top: 49px;
    font-size: 11px; color: var(--ink);
  }
  .contact-list {
    position: absolute; left: 30px; top: 92px;
    list-style: none;
  }
  .contact-list li {
    display: flex; align-items: center; gap: 8px;
    font-size: 11.5px; color: var(--ink); line-height: 19px;
  }
  .contact-list svg { width: 10px; height: 10px; fill: var(--sky-deep); }
  .alumni-badge {
    position: absolute; left: 30px; top: 170px;
    width: 62px; height: 40px; border-radius: 3px;
    background: var(--badge-gold);
  }
  .cert-row {
    position: absolute; left: 104px; top: 190px;
    display: flex; gap: 14px; align-items: flex-end;
  }
  .cert-badge {
    width: 70px; height: 30px; border-radius: 3px;
    background: var(--badge-grey);
  }
  .cert-row .cert-badge:nth-child(2) { margin-bottom: 14px; }
  .cert-row .cert-badge:nth-child(3) { margin-bottom: 28px; }
  .cert-row .cert-badge:nth-child(4) { margin-bottom: 42px; }
  .front-brand {
    position: absolute; right: 30px; top: 112px;
    text-align: right;
  }
  .brand-line { display: flex; align-items: center; gap: 10px; justify-content: flex-end; }
  .brand-dot { width: 26px; height: 26px; border-radius: 50%; }
  .front-brand .brand-dot { background: var(--sky); }
  .front-brand .brand-name {
    font-size: 24px; font-weight: 400; color: var(--sky-deep);
  }
  .front-brand .brand-tagline {
    font-size: 9px; letter-spacing: 2px; text-transform: uppercase;
    color: var(--ink-soft); margin-top: 2px;
  }

  /* ---------- Back (brand side) ---------- */
  .card-back {
    left: 630px;
    top: 300px;
    background: var(--sky);
    color: var(--white);
  }
  .back-brand {
    position: absolute; left: 0; right: 0; top: 96px;
    text-align: center;
  }
  .back-brand .brand-line { justify-content: center; }
  .back-brand .brand-dot { border: 2px solid var(--white); }
  .back-brand .brand-name { font-size: 30px; font-weight: 400; color: var(--white); }
  .back-brand .brand-tagline {
    font-size: 10px; letter-spacing: 2.5px; text-transform: uppercase;
    color: var(--white); margin-top: 4px;
  }
  .service-list {
    position: absolute; left: 0; right: 0; top: 184px;
    display: flex; justify-content: center; gap: 28px;
    list-style: none; font-size: 13px; color: var(--white);
  }
  .service-list li::before { content: "\2022"; margin-right: 8px; }
</style>
</head>
<body>

  <section class="card card-front">
    <h1 class="holder-name">NANNA</h1>
    <p class="holder-role">Director</p>
    <ul class="contact-list">
      <li><svg viewBox="0 0 10 10"><path d="M2 0h2l1 3-1.5 1a6 6 0 0 0 2.5 2.5L7 5l3 1v2c0 1-1 2-2 2C4 10 0 6 0 2 0 1 1 0 2 0z"/></svg>407-555-0192</li>
      <li><svg viewBox="0 0 10 10"><path d="M0 2h10v6H0z M0 2l5 3 5-3" /></svg>nanna.keyplate@inboxmail.net</li>
      <li><svg viewBox="0 0 10 10"><circle cx="5" cy="5" r="5"/></svg>www.nanna-keyplate.com</li>
    </ul>
    <div class="alumni-badge" role="img" aria-label="KMB Alumni badge"></div>
    <div class="cert-row">
      <div class="cert-badge" role="img" aria-label="Certification badge"></div>
      <div class="cert-badge" role="img" aria-label="Certification badge"></div>
      <div class="cert-badge" role="img" aria-label="Certification badge"></div>
      <div class="cert-badge" role="img" aria-label="Certification badge"></div>
    </div>
    <div class="front-brand">
      <div class="brand-line"><span class="brand-dot"></span><span class="brand-name">Nanna Keyplate</span></div>
      <p class="brand-tagline">Cherish Every Gadget</p>
    </div>
  </section>

  <section class="card card-back">
    <div class="back-brand">
      <div class="brand-line"><span class="brand-dot"></span><span class="brand-name">Nanna Keyplate</span></div>
      <p class="brand-tagline">Cherish Every Gadget</p>
    </div>
    <ul class="service-list">
      <li>Desktops</li>
      <li>Laptops</li>
      <li>Handhelds</li>
    </ul>
  </section>

</body>
</html>
```